Sunny Meadow Folk - HEMP Products store

Sunny Meadow Folk sell the best hemp products on the market online and at markets and expos Australia wide. Our products are mostly cosmetics, oils, lotions, plus some miscellaneous items such as as bags, clothing, household goods. We would like the website to be lighthearted, fun and portray health and happiness.
We don't want too much information on the main page/home page mostly links and buttons and images.
Things to include: buttons that lead to further info and blog. I would like the buttons for info to have a tiny bit of writing on them to entice people to click for the further info they actually want.
What's on section.
About us
Slideshow of featured products
subscription section
sign up for newsletter link.
Contact us link
Feedback section
Shop & shopping cart etc
short blog section with room to add images
spot for video tutorials
useful links.
connect to social media
And any other cool fun stuff you can think of for us.
We currently have a domain with NetHarbor and they use platform Site Crafter 4
www.sunnymeadowfolk.com.au
info@sunnymeadowfolk.com.au
Please see our Logo attached.
I also attached a very badly drawn example of a layout that I like

Target Market(s)

All ages. Parents. Health conscious buyers. natural product consumers. Environmentalist.

Coding

Coded - Design and coding required

Number of Pages Required

5+ page

Font styles to use
Sans Serif
Other font styles liked:
• Wobblyn lass font. http://www.typebarn.com/wobblyn-lass.font

Requirements
Nice to have
• green drop shaped buttons - similar shape to the characters.
Should not have
• Prominent pictures of marijuana leaves.

```html
<!DOCTYPE html>
<html lang="en">
<head>
<meta charset="utf-8">
<title>Sunny Meadow Folk – Hemp Products</title>
<link rel="stylesheet" href="https://fonts.googleapis.com/css2?family=Open+Sans:ital,wght@0,400;0,600;0,700;0,800;1,400;1,600&display=swap">
<style>
:root{
  --green:#3a9a3e;
  --green-dark:#2e7f32;
  --green-light:#9ac43b;
  --lime:#a6d456;
  --ink:#222;
  --text:#555;
  --muted:#888;
  --rule:#e2e2e2;
  --grey-bg:#ebebeb;
  --soft-bg:#f4f4f4;
  --dark:#3a3a3a;
}
*{box-sizing:border-box;margin:0;padding:0}
html,body{width:1200px;height:3327px;overflow:hidden}
body{position:relative;background:#fff;font-family:"Open Sans",Arial,sans-serif;color:var(--text)}
.abs{position:absolute}
section,header,footer{position:absolute;left:0;width:1200px}

/* header */
.site-header{top:0;height:133px;background:#fff}
.brand{left:78px;top:22px;width:110px;font-weight:800;font-size:21px;line-height:24px;color:var(--ink);text-transform:uppercase}
.search{left:472px;top:22px;width:271px;height:33px;border:1px solid #d6d6d6;border-radius:3px;font-size:13px;color:#999;padding:7px 12px}
.search svg{position:absolute;right:10px;top:8px}
.util{top:22px;height:33px;display:flex;align-items:center;gap:9px;font-size:13px;font-weight:600;color:#333;text-transform:uppercase}
.util .ring{width:32px;height:32px;border:2px solid var(--green);border-radius:50%;display:flex;align-items:center;justify-content:center}
.util .count{color:var(--green)}
.main-nav{top:85px;left:244px;height:28px;display:flex;align-items:center;font-size:13px;font-weight:600;color:#333;text-transform:uppercase}
.main-nav a{position:absolute;white-space:nowrap;color:#333;text-decoration:none}
.main-nav a.active{color:var(--green)}
.btn-blog,.btn-info{position:absolute;top:80px;height:37px;color:#fff;font-size:13px;font-weight:700;display:flex;align-items:center;justify-content:center;border-radius:2px}
.btn-blog{left:965px;width:73px;background:var(--dark)}
.btn-info{left:1049px;width:75px;background:linear-gradient(#5cb85c,var(--green-dark))}

/* hero */
.hero{top:133px;height:524px;background:radial-gradient(ellipse at 50% 40%,#9a8763 0%,#7d6a4c 45%,#5a4a36 100%)}
.hero-logo{left:495px;top:69px;width:208px;height:208px;border-radius:50%;background:#f5f3ee;display:flex;align-items:center;justify-content:center;text-align:center;font-weight:800;font-size:28px;line-height:32px;color:var(--ink);text-transform:uppercase}
.hero-text{left:0;width:1200px;top:296px;text-align:center;color:#fff;font-weight:700;font-size:20px;line-height:31px;text-transform:uppercase;text-shadow:0 1px 3px rgba(0,0,0,.45)}
.btn-shop{left:506px;top:384px;width:191px;height:38px;background:var(--green);color:#fff;font-weight:700;font-size:18px;display:flex;align-items:center;justify-content:center;text-transform:uppercase}
.hero-arrow{top:247px}

/* about */
.about{top:657px;height:470px;background:var(--grey-bg)}
.section-title{font-weight:700;font-size:29px;color:var(--ink);text-transform:uppercase;white-space:nowrap}
.about .section-title{left:0;width:1200px;text-align:center;top:68px}
.about-copy{left:88px;width:1024px;top:126px;text-align:center;font-size:14px;line-height:29px;color:#666}
.drop-link{top:235px;width:150px;text-align:center}
.drop-link svg{display:block;margin:0 auto}
.drop-link .label{margin-top:14px;font-size:15px;font-weight:700;color:#333;line-height:20px;text-transform:uppercase}
.drop-link .label.accent{color:var(--green)}
.drop-link .hint{font-size:10px;font-weight:600;color:#666;text-transform:uppercase}

/* products */
.products{top:1127px;height:510px;background:#fff}
.products .h-cat{left:75px;top:45px;font-size:22px}
.products .h-feat{left:591px;top:39px;font-size:29px}
.pager{display:flex;gap:6px}
.pager span{width:24px;height:24px;border-radius:50%;background:#8a8a8a;display:flex;align-items:center;justify-content:center}
.cat-list{left:75px;top:106px;width:242px;height:355px;border:1px solid var(--rule)}
.cat-list li{list-style:none;height:69px;border-bottom:1px solid var(--rule);display:flex;align-items:center;padding-left:24px;gap:12px;font-size:14px;font-weight:600;color:#333;text-transform:uppercase}
.cat-list li:last-child{border-bottom:0}
.cat-list li.active{color:var(--green)}
.card{top:106px;width:270px;height:355px;border:1px solid var(--rule)}
.card .photo{position:absolute;left:30px;top:14px;width:210px;height:150px}
.card .name{position:absolute;left:18px;top:172px;font-size:14px;font-weight:700;color:var(--green);text-transform:uppercase}
.card .desc{position:absolute;left:18px;top:196px;width:180px;font-size:14px;line-height:24px;color:#666}
.card .rate{position:absolute;left:18px;top:260px;display:flex;align-items:center;gap:12px;font-size:14px;color:#333}
.card .rate i{width:24px;height:24px;background:var(--green);display:flex;align-items:center;justify-content:center}
.card .price{position:absolute;left:18px;top:296px;font-size:22px;font-weight:600;color:#333}
.card .price s{font-size:14px;color:#888;font-weight:400;margin-right:4px}
.card .tools{position:absolute;right:0;top:236px;width:45px;height:118px;border-left:1px solid var(--rule)}
.card .tools span{height:39px;display:flex;align-items:center;justify-content:center;border-bottom:1px solid var(--rule)}
.card .tools span:last-child{border-bottom:0}

/* events + video */
.events{top:1637px;height:435px;background:var(--soft-bg)}
.events .h-on{left:75px;top:40px}
.events .h-vid{left:614px;top:40px}
.event{left:75px;width:512px;border-bottom:1px solid #ddd;padding-bottom:14px}
.event .date{font-size:14px;font-weight:700;color:var(--green);text-transform:uppercase}
.event p{margin-top:8px;font-size:13.5px;line-height:26px;color:#555}
.event p em{font-style:italic;font-weight:600;color:#333}
.video{left:614px;top:95px;width:513px;height:278px;background:linear-gradient(135deg,#e9e7e0,#cfcabd 50%,#8c7a2c 85%)}
.video .play{position:absolute;left:220px;top:110px;width:74px;height:52px;border-radius:8px;background:rgba(255,255,255,.85);display:flex;align-items:center;justify-content:center}

/* blog */
.blog{top:2072px;height:474px;background:#fff}
.blog .section-title{left:0;width:1200px;top:41px;display:flex;justify-content:center;align-items:center;gap:14px}
.post-date{top:119px;width:149px;height:49px;background:var(--dark);color:#fff;font-size:20px;font-weight:600;display:flex;align-items:center;justify-content:center;gap:14px;text-transform:uppercase}
.post-title{top:195px;width:200px;font-size:17px;line-height:29px;font-weight:700;color:var(--green);text-transform:uppercase}
.post-text{top:283px;width:220px;font-size:14px;line-height:24px;color:#555}
.post-more{top:388px;font-size:13px;font-style:italic;font-weight:600;color:#333}
.post-photo{top:119px;width:282px;height:284px}

/* feedback */
.feedback{top:2546px;height:408px;background:linear-gradient(180deg,#9fd25a 0%,#bfe27d 50%,#e7f4cf 100%)}
.feedback .section-title{left:0;width:1200px;text-align:center;top:40px}
.quote{top:115px;width:330px}
.quote p{font-size:14.5px;line-height:26px;font-style:italic;color:#333}
.quote .mark{margin-top:26px;font-size:40px;font-weight:800;color:var(--green);line-height:20px;height:20px}
.quote .who{margin-top:22px;display:flex;align-items:center;gap:18px}
.quote .avatar{width:72px;height:72px;border-radius:50%;border:3px solid #fff}
.quote .who b{display:block;font-size:13px;color:var(--green);text-transform:uppercase}
.quote .who small{font-size:12px;color:#333}

/* footer */
.site-footer{top:2954px;height:289px;background:#fff;border-top:4px solid var(--green)}
.f-col{top:54px}
.f-col h4{font-size:17px;font-weight:700;color:#222;margin-bottom:16px}
.f-col li{list-style:none;font-size:12.5px;line-height:30px;color:#555}
.f-rule{top:54px;width:1px;height:190px;background:var(--rule)}
.subscribe-note{font-size:12.5px;color:#555;margin-bottom:16px}
.subscribe{display:flex;width:348px;height:36px}
.subscribe span{flex:1;border:1px solid #ccc;font-size:12.5px;color:#777;padding:9px 12px}
.subscribe b{width:99px;background:var(--green-light);color:#fff;font-size:12px;display:flex;align-items:center;justify-content:center;text-transform:uppercase}
.social{display:flex;gap:12px;margin-top:14px}
.social span{width:38px;height:38px;border-radius:50%}
.copyright{position:absolute;left:0;top:3243px;width:1200px;height:84px;background:#fff;border-top:1px solid var(--rule);text-align:center;font-size:12.5px;color:#555;padding-top:32px}
</style>
</head>
<body>

<header class="site-header">
  <div class="abs brand">Sunny Meadow Folk</div>
  <div class="abs search">Search...
    <svg width="16" height="16" viewBox="0 0 16 16"><circle cx="6.5" cy="6.5" r="5" fill="none" stroke="#3a9a3e" stroke-width="2"/><line x1="10.5" y1="10.5" x2="15" y2="15" stroke="#3a9a3e" stroke-width="2.2"/></svg>
  </div>
  <div class="abs util" style="left:772px"><span class="ring"><svg width="14" height="12" viewBox="0 0 14 12"><rect x="1" y="1" width="12" height="10" rx="1" fill="none" stroke="#3a9a3e" stroke-width="1.6"/><path d="M1 2l6 5 6-5" fill="none" stroke="#3a9a3e" stroke-width="1.6"/></svg></span>Sign up for newsletter</div>
  <div class="abs util" style="left:1009px"><span class="ring"><svg width="16" height="14" viewBox="0 0 16 14"><path d="M1 1h3l2 8h8l1-6H5" fill="none" stroke="#3a9a3e" stroke-width="1.6"/><circle cx="7" cy="12" r="1.3" fill="#3a9a3e"/><circle cx="13" cy="12" r="1.3" fill="#3a9a3e"/></svg></span>My Cart <span class="count">(0)</span></div>
  <nav class="abs main-nav">
    <a class="active" style="left:0">Home</a>
    <a style="left:80px">About Us</a>
    <a style="left:186px">Products</a>
    <a style="left:299px">What's On</a>
    <a style="left:412px">Shop</a>
    <a style="left:488px">Useful Links</a>
    <a style="left:621px">Contact Us</a>
  </nav>
  <div class="btn-blog">BLOG</div>
  <div class="btn-info">INFO</div>
</header>

<section class="hero" role="img" aria-label="Hemp seeds in a wooden spoon and sack beside a bottle of hemp oil">
  <div class="abs hero-logo">Sunny<br>Meadow<br>Folk</div>
  <div class="abs hero-text">Sunny Meadow Folk sell the best hemp products on the market<br>online and at markets and expos Australia wide.</div>
  <div class="abs btn-shop">Shop Now</div>
  <svg class="abs hero-arrow" style="left:62px" width="22" height="36" viewBox="0 0 22 36"><path d="M18 3L4 18l14 15" fill="none" stroke="#fff" stroke-width="5"/></svg>
  <svg class="abs hero-arrow" style="left:1114px" width="22" height="36" viewBox="0 0 22 36"><path d="M4 3l14 15L4 33" fill="none" stroke="#fff" stroke-width="5"/></svg>
</section>

<section class="about">
  <h2 class="abs section-title">About Sunny Meadow Folk</h2>
  <p class="abs about-copy">On the other hand, we denounce with righteous indignation and dislike men who are so beguiled and demoralized by the charms of pleasure of the moment, so blinded by desire, that they cannot foresee the pain and trouble that are bound to ensue; and equal blame belongs</p>

  <div class="abs drop-link" style="left:69px"><svg width="64" height="84" viewBox="0 0 64 84"><path d="M32 2C32 2 4 36 4 54a28 28 0 0056 0C60 36 32 2 32 2z" fill="#3a9a3e"/><circle cx="32" cy="54" r="7" fill="none" stroke="#fff" stroke-width="3"/></svg><div class="label accent">More About Us</div></div>
  <div class="abs drop-link" style="left:258px"><svg width="64" height="84" viewBox="0 0 64 84"><path d="M32 2C32 2 4 36 4 54a28 28 0 0056 0C60 36 32 2 32 2z" fill="#3a9a3e"/><rect x="24" y="50" width="16" height="11" fill="#fff"/><rect x="22" y="45" width="20" height="5" fill="#fff"/></svg><div class="label">Free Stuff</div><div class="hint">Win win win</div></div>
  <div class="abs drop-link" style="left:446px"><svg width="64" height="84" viewBox="0 0 64 84"><path d="M32 2C32 2 4 36 4 54a28 28 0 0056 0C60 36 32 2 32 2z" fill="#3a9a3e"/><circle cx="26" cy="60" r="2.5" fill="#fff"/><path d="M25 50a10 10 0 0110 10M25 44a16 16 0 0116 16" fill="none" stroke="#fff" stroke-width="3"/></svg><div class="label">Product<br>Subscription</div></div>
  <div class="abs drop-link" style="left:635px"><svg width="64" height="84" viewBox="0 0 64 84"><path d="M32 2C32 2 4 36 4 54a28 28 0 0056 0C60 36 32 2 32 2z" fill="#3a9a3e"/><circle cx="32" cy="49" r="5" fill="#fff"/><path d="M23 63a9 8 0 0118 0z" fill="#fff"/></svg><div class="label">Quality<br>Assurance</div></div>
  <div class="abs drop-link" style="left:823px"><svg width="64" height="84" viewBox="0 0 64 84"><path d="M32 2C32 2 4 36 4 54a28 28 0 0056 0C60 36 32 2 32 2z" fill="#3a9a3e"/><circle cx="32" cy="54" r="9" fill="none" stroke="#fff" stroke-width="3"/><line x1="23" y1="54" x2="41" y2="54" stroke="#fff" stroke-width="2"/></svg><div class="label">Support</div></div>
  <div class="abs drop-link" style="left:1012px"><svg width="64" height="84" viewBox="0 0 64 84"><path d="M32 2C32 2 4 36 4 54a28 28 0 0056 0C60 36 32 2 32 2z" fill="#3a9a3e"/><circle cx="32" cy="54" r="9" fill="#fff"/><rect x="30.5" y="52" width="3" height="7" fill="#3a9a3e"/><circle cx="32" cy="49" r="1.6" fill="#3a9a3e"/></svg><div class="label">Further<br>Info</div></div>
</section>

<section class="products">
  <h2 class="abs section-title h-cat">Product Categories</h2>
  <div class="abs" style="left:591px;top:39px;display:flex;align-items:center;gap:16px">
    <h2 class="section-title" style="font-size:29px">Featured Product</h2>
    <div class="pager"><span><svg width="10" height="10" viewBox="0 0 10 10"><path d="M7 1L3 5l4 4" fill="none" stroke="#fff" stroke-width="2"/></svg></span><span><svg width="10" height="10" viewBox="0 0 10 10"><path d="M3 1l4 4-4 4" fill="none" stroke="#fff" stroke-width="2"/></svg></span></div>
  </div>
  <ul class="abs cat-list">
    <li class="active"><svg width="12" height="16" viewBox="0 0 12 16"><path d="M6 0C6 0 0 8 0 10a6 6 0 0012 0C12 8 6 0 6 0z" fill="#3a9a3e"/></svg>Oils</li>
    <li><svg width="12" height="16" viewBox="0 0 12 16"><path d="M6 0C6 0 0 8 0 10a6 6 0 0012 0C12 8 6 0 6 0z" fill="#666"/></svg>Lotions</li>
    <li><svg width="12" height="16" viewBox="0 0 12 16"><path d="M6 0C6 0 0 8 0 10a6 6 0 0012 0C12 8 6 0 6 0z" fill="#666"/></svg>Plus</li>
    <li><svg width="12" height="16" viewBox="0 0 12 16"><path d="M6 0C6 0 0 8 0 10a6 6 0 0012 0C12 8 6 0 6 0z" fill="#666"/></svg>Clothing</li>
    <li><svg width="12" height="16" viewBox="0 0 12 16"><path d="M6 0C6 0 0 8 0 10a6 6 0 0012 0C12 8 6 0 6 0z" fill="#666"/></svg>Household Goods</li>
  </ul>

  <div class="abs card" style="left:338px">
    <div class="photo" role="img" aria-label="Hemp shopping bag filled with fresh vegetables" style="background:linear-gradient(160deg,#f4efe6,#d9c4a0 60%,#7fae4a)"></div>
    <div class="name">Product Name</div>
    <div class="desc">Duis aliquam nibh a dui iaculis viverra</div>
    <div class="rate"><i><svg width="12" height="12" viewBox="0 0 12 12"><path d="M6 0l1.8 4 4.2.4-3.2 2.8 1 4.2L6 9.2 2.2 11.4l1-4.2L0 4.4 4.2 4z" fill="#fff"/></svg></i>4.3</div>
    <div class="price"><s>$12.00</s>$10.00</div>
    <div class="tools"><span><svg width="14" height="12" viewBox="0 0 16 14"><path d="M1 1h3l2 8h8l1-6H5" fill="none" stroke="#3a9a3e" stroke-width="2"/><circle cx="7" cy="12" r="1.5" fill="#3a9a3e"/><circle cx="13" cy="12" r="1.5" fill="#3a9a3e"/></svg></span><span><svg width="14" height="10" viewBox="0 0 14 10"><path d="M1 5c3-5 9-5 12 0-3 5-9 5-12 0z" fill="#aaa"/><circle cx="7" cy="5" r="2" fill="#fff"/></svg></span><span><svg width="14" height="12" viewBox="0 0 14 12"><path d="M7 11L1.5 5.5A3 3 0 017 2a3 3 0 015.5 3.5z" fill="#aaa"/></svg></span></div>
  </div>
  <div class="abs card" style="left:607px">
    <div class="photo" role="img" aria-label="Bars of natural hemp soap on a blue soap dish" style="background:linear-gradient(180deg,#f3eee6,#e0cfae 55%,#5aa6d6)"></div>
    <div class="name">Product Name</div>
    <div class="desc">Duis aliquam nibh a dui iaculis viverra</div>
    <div class="rate"><i><svg width="12" height="12" viewBox="0 0 12 12"><path d="M6 0l1.8 4 4.2.4-3.2 2.8 1 4.2L6 9.2 2.2 11.4l1-4.2L0 4.4 4.2 4z" fill="#fff"/></svg></i>4.3</div>
    <div class="price"><s>$12.00</s>$10.00</div>
    <div class="tools"><span><svg width="14" height="12" viewBox="0 0 16 14"><path d="M1 1h3l2 8h8l1-6H5" fill="none" stroke="#3a9a3e" stroke-width="2"/><circle cx="7" cy="12" r="1.5" fill="#3a9a3e"/><circle cx="13" cy="12" r="1.5" fill="#3a9a3e"/></svg></span><span><svg width="14" height="10" viewBox="0 0 14 10"><path d="M1 5c3-5 9-5 12 0-3 5-9 5-12 0z" fill="#aaa"/><circle cx="7" cy="5" r="2" fill="#fff"/></svg></span><span><svg width="14" height="12" viewBox="0 0 14 12"><path d="M7 11L1.5 5.5A3 3 0 017 2a3 3 0 015.5 3.5z" fill="#aaa"/></svg></span></div>
  </div>
  <div class="abs card" style="left:887px;width:240px">
    <div class="photo" role="img" aria-label="Hemp balm tin with a bottle of hemp oil" style="left:20px;background:linear-gradient(180deg,#fafafa,#e8e4dc 50%,#3b3a33)"></div>
    <div class="name">Product Name</div>
    <div class="desc">Duis aliquam nibh a dui iaculis viverra</div>
    <div class="rate"><i><svg width="12" height="12" viewBox="0 0 12 12"><path d="M6 0l1.8 4 4.2.4-3.2 2.8 1 4.2L6 9.2 2.2 11.4l1-4.2L0 4.4 4.2 4z" fill="#fff"/></svg></i>4.3</div>
    <div class="price"><s>$12.00</s>$10.00</div>
    <div class="tools"><span><svg width="14" height="12" viewBox="0 0 16 14"><path d="M1 1h3l2 8h8l1-6H5" fill="none" stroke="#3a9a3e" stroke-width="2"/><circle cx="7" cy="12" r="1.5" fill="#3a9a3e"/><circle cx="13" cy="12" r="1.5" fill="#3a9a3e"/></svg></span><span><svg width="14" height="10" viewBox="0 0 14 10"><path d="M1 5c3-5 9-5 12 0-3 5-9 5-12 0z" fill="#aaa"/><circle cx="7" cy="5" r="2" fill="#fff"/></svg></span><span><svg width="14" height="12" viewBox="0 0 14 12"><path d="M7 11L1.5 5.5A3 3 0 017 2a3 3 0 015.5 3.5z" fill="#aaa"/></svg></span></div>
  </div>
</section>

<section class="events">
  <h2 class="abs section-title h-on">What's On</h2>
  <h2 class="abs section-title h-vid">Video Tutorials</h2>
  <div class="abs event" style="top:92px"><div class="date">Mar 20, 2017</div><p>Duis aliquam nibh a dui iaculis viverra ante ipsum primis in faucibus orci luctus et ultrices posuere cubilia.. <em>Read More</em></p></div>
  <div class="abs event" style="top:201px"><div class="date">Mar 20, 2017</div><p>Duis aliquam nibh a dui iaculis viverra ante ipsum primis in faucibus orci luctus et ultrices posuere cubilia.. <em>Read More</em></p></div>
  <div class="abs event" style="top:310px;border-bottom:0"><div class="date">Mar 20, 2017</div><p>Duis aliquam nibh a dui iaculis viverra ante ipsum primis in faucibus orci luctus et ultrices posuere cubilia.. <em>Read More</em></p></div>
  <div class="abs video" role="img" aria-label="Video still of hemp oil pouring onto a spoon">
    <div class="play"><svg width="24" height="26" viewBox="0 0 24 26"><path d="M2 1l21 12L2 25z" fill="#444"/></svg></div>
  </div>
</section>

<section class="blog">
  <h2 class="abs section-title">Latest Blog <span class="pager"><span><svg width="10" height="10" viewBox="0 0 10 10"><path d="M7 1L3 5l4 4" fill="none" stroke="#fff" stroke-width="2"/></svg></span><span><svg width="10" height="10" viewBox="0 0 10 10"><path d="M3 1l4 4-4 4" fill="none" stroke="#fff" stroke-width="2"/></svg></span></span></h2>

  <div class="abs post-date" style="left:75px">March <span>18</span></div>
  <div class="abs post-title" style="left:75px">Nam fermentum vestibulum purus id aliquet</div>
  <div class="abs post-text" style="left:75px">Duis aliquam nibh a dui iaculis viverra ante ipsum primis in faucibus orci luctus et ultrices posuere cubilia..</div>
  <div class="abs post-more" style="left:75px">Continue Reading</div>
  <div class="abs post-photo" role="img" aria-label="Hemp seeds, seed bar and a jar of hemp oil on a table" style="left:306px;background:linear-gradient(160deg,#6b4a2c,#c39a5a 45%,#8a4a22)"></div>

  <div class="abs post-date" style="left:614px">April <span>20</span></div>
  <div class="abs post-title" style="left:614px">Nam fermentum vestibulum purus id aliquet</div>
  <div class="abs post-text" style="left:614px">Duis aliquam nibh a dui iaculis viverra ante ipsum primis in faucibus orci luctus et ultrices posuere cubilia..</div>
  <div class="abs post-more" style="left:614px">Continue Reading</div>
  <div class="abs post-photo" role="img" aria-label="Bottles of hemp oil and capsules among green plants" style="left:845px;background:linear-gradient(160deg,#a9c37a,#e8eee0 50%,#4f7a3a)"></div>
</section>

<section class="feedback">
  <h2 class="abs section-title">Customers Feedback</h2>
  <div class="abs quote" style="left:78px"><p>" Duis aliquam nibh a dui iaculis viverra ante ipsum primis in faucibus orci luctus et ultrices posuere cubilia a nibh eget turpis vehicula tempus ac sed massa..."</p><div class="mark">“</div><div class="who"><div class="avatar" role="img" aria-label="Customer portrait" style="background:#d9b79a"></div><div><b>Name Heading</b><small>Location</small></div></div></div>
  <div class="abs quote" style="left:437px"><p>" Duis aliquam nibh a dui iaculis viverra ante ipsum primis in faucibus orci luctus et ultrices posuere cubilia a nibh eget turpis vehicula tempus ac sed massa..."</p><div class="mark">“</div><div class="who"><div class="avatar" role="img" aria-label="Customer portrait" style="background:#6a5446"></div><div><b>Name Heading</b><small>Location</small></div></div></div>
  <div class="abs quote" style="left:794px"><p>" Duis aliquam nibh a dui iaculis viverra ante ipsum primis in faucibus orci luctus et ultrices posuere cubilia a nibh eget turpis vehicula tempus ac sed massa..."</p><div class="mark">“</div><div class="who"><div class="avatar" role="img" aria-label="Customer portrait" style="background:#c9a48a"></div><div><b>Name Heading</b><small>Location</small></div></div></div>
</section>

<footer class="site-footer">
  <div class="abs f-col" style="left:78px"><h4>Quick Links</h4><ul><li>About Us</li><li>Careers</li><li>Privacy &amp; Security</li><li>Site Map</li><li>Terms of Use</li><li>Blog</li></ul></div>
  <div class="abs f-rule" style="left:252px"></div>
  <div class="abs f-col" style="left:275px"><h4>Help &amp; support</h4><ul><li>Recommended Reading</li><li>Submit your Story</li><li>Contact Us</li><li>Frequently Asked Questions</li><li>How to Order</li></ul></div>
  <div class="abs f-rule" style="left:490px"></div>
  <div class="abs f-col" style="left:548px"><h4>My Account</h4><ul><li>Delivery Information</li><li>My Account</li><li>Order Tracking</li><li>Reminder Service</li><li>Shipping, Returns &amp; Fees</li></ul></div>
  <div class="abs f-rule" style="left:727px"></div>
  <div class="abs f-col" style="left:776px">
    <h4>Email Subscription</h4>
    <p class="subscribe-note">Register your email address to get information about us</p>
    <div class="subscribe"><span>Email Address</span><b>Subscribe</b></div>
    <h4 style="margin:18px 0 0">Stay Connected</h4>
    <div class="social">
      <span style="background:#43b06a"></span><span style="background:#3b5998"></span><span style="background:#38a1f3"></span><span style="background:#dd4b39"></span><span style="background:#4a7cae"></span><span style="background:#3aa6d8"></span><span style="background:#2b8fc3"></span><span style="background:#cc181e"></span><span style="background:#c8232c"></span>
    </div>
  </div>
</footer>
<div class="copyright">Copyright © 2017. Company Name.All right Reserved</div>

</body>
</html>
```